Tincture Design for Woman Owned CBD Branf

LumiVelle is a luxery CBD brand for millennial women.

Our premium L Oil contains 500mg of full spectrum CBD derived from specially-sourced hemp for unparalleled purity and quality. Each dropper delivers approximately 20mg of CBD. Available in two flavors, Natural and Mint.

The goal is to design an aesthetically pleasing tincture (bottle dropper) with label and box. The final design should coincide with our brand guidelines and easily marketed for beauty consumers. We are looking for a clean design, the use of raised fonts and/or metallic is fine.

We have 4 other designs we'd like to work on with the winning designer.

Target Market(s)

Millennial Women, Income $75k+

Font styles to use
Other font styles liked:
• See Branding Sheet

Requirements
Must have
• Must follow brand guidelines (see attached for colors, font, etc)
Nice to have
• Raised font or Metallic Print

```html
<!DOCTYPE html>
<html lang="en">
<head>
<meta charset="utf-8">
<title>LumiVelle Full Spectrum CBD – Box and Label</title>
<link rel="stylesheet" href="https://fonts.googleapis.com/css2?family=Playfair+Display:wght@400;500&family=Barlow:wght@400&family=Montserrat:wght@700;800&family=Pathway+Gothic+One&display=swap">
<style>
  :root {
    --bg: #e4e4e4;
    --green: #226f5c;
    --green-dark: #0f4a3c;
    --green-light: #2d8069;
    --gold: #c9a15a;
    --gold-dark: #a87d34;
    --gold-light: #d8b46e;
    --white: #f7f7f5;
    --ink: #2a2a2a;
  }
  * { margin: 0; padding: 0; box-sizing: border-box; }
  html, body { width: 1200px; height: 1200px; overflow: hidden; background: var(--bg); }
  .canvas { position: relative; width: 1200px; height: 1200px; }

  .serif { font-family: "Playfair Display", serif; }
  .condensed { font-family: "Pathway Gothic One", sans-serif; }

  /* ---------- Box dieline ---------- */
  .box { position: absolute; left: 60px; top: 100px; width: 560px; height: 1000px; display: flex; box-shadow: 0 10px 30px rgba(0,0,0,.12); }
  .panel { position: relative; height: 100%; display: flex; flex-direction: column; }
  .panel--side { width: 230px; border-right: 1px solid rgba(0,0,0,.12); }
  .panel--front { width: 330px; }

  .zone-green { position: relative; height: 440px; background: linear-gradient(160deg, var(--green-light), var(--green) 55%, var(--green-dark)); overflow: hidden; }
  .zone-gold { height: 170px; background: linear-gradient(90deg, var(--gold-dark), var(--gold) 40%, var(--gold-light)); border-top: 3px solid var(--white); }
  .zone-white { position: relative; flex: 1; background: var(--white); }

  .leaf-mark { position: absolute; inset: 20px 10px 0; background: radial-gradient(ellipse at 50% 60%, rgba(20,80,64,.35), rgba(20,80,64,0) 70%); }

  .brand-seal { position: absolute; left: 50%; transform: translateX(-50%); display: flex; align-items: center; justify-content: center; border: 1.5px solid rgba(247,247,245,.85); border-radius: 50%; }
  .brand-name { font-family: "Playfair Display", serif; font-weight: 400; color: var(--white); letter-spacing: .04em; }

  .front-seal { top: 190px; width: 240px; height: 205px; }
  .front-seal .brand-name { font-size: 40px; }

  .side-seal { top: 85px; width: 90px; height: 170px; }
  .side-seal .brand-name { font-size: 17px; writing-mode: horizontal-tb; }

  .warning { position: absolute; left: 22px; right: 22px; top: 283px; font-size: 11.5px; line-height: 1.45; color: var(--white); text-align: justify; }

  .front-gold { display: flex; flex-direction: column; align-items: center; justify-content: center; color: var(--white); }
  .front-gold .kicker { font-size: 25px; letter-spacing: .02em; line-height: 1; }
  .front-gold .title { font-size: 108px; font-weight: 500; line-height: 1; margin-top: 4px; }

  .side-gold { display: flex; align-items: center; justify-content: center; gap: 14px; }
  .badge { width: 82px; height: 82px; border-radius: 50%; border: 2px solid var(--white); background: rgba(255,255,255,.12); }

  .claim { font-family: "Barlow", sans-serif; color: var(--ink); text-align: center; line-height: 1.3; }
  .dose-pill { display: flex; flex-direction: column; align-items: center; justify-content: center; background: var(--green); color: var(--white); border-radius: 50%; font-family: "Montserrat", sans-serif; font-weight: 800; line-height: 1; }
  .flavour { font-family: "Montserrat", sans-serif; font-weight: 700; text-align: center; }
  .supplement { position: absolute; left: 50%; transform: translateX(-50%); display: flex; align-items: center; justify-content: center; background: var(--gold); color: var(--white); border-radius: 10px 10px 0 0; font-family: "Playfair Display", serif; letter-spacing: .04em; white-space: nowrap; }

  .front-white .claim { position: absolute; top: 45px; left: 0; right: 0; font-size: 21px; }
  .front-white .dose-pill { position: absolute; top: 130px; left: 50%; transform: translateX(-50%); width: 200px; height: 92px; }
  .front-white .dose-pill .mg { font-size: 34px; }
  .front-white .dose-pill .thc { font-size: 26px; margin-top: 2px; }
  .front-white .flavour { position: absolute; top: 258px; left: 0; right: 0; font-size: 19px; color: var(--green); }
  .front-white .supplement { bottom: 0; width: 280px; height: 52px; font-size: 19px; }

  .side-copy { position: absolute; left: 20px; right: 20px; font-size: 13px; line-height: 1.45; color: var(--green-dark); text-align: center; }
  .side-copy--store { top: 40px; }
  .side-copy--use { top: 118px; }
  .fda-box { position: absolute; left: 18px; right: 18px; top: 210px; border: 1.5px solid var(--ink); padding: 10px 8px; font-size: 11.5px; line-height: 1.4; color: var(--ink); text-align: center; }
  .side-white .supplement { bottom: 0; width: 180px; height: 48px; font-size: 14px; }

  /* ---------- Bottle label ---------- */
  .label { position: absolute; left: 690px; top: 255px; width: 450px; height: 690px; display: flex; flex-direction: column; box-shadow: 0 10px 30px rgba(0,0,0,.12); }
  .label .zone-green { height: 335px; }
  .label-seal { top: 58px; width: 320px; height: 235px; }
  .label-seal .brand-name { font-size: 46px; }
  .label-band { height: 80px; border-top: 4px solid var(--white); background: linear-gradient(90deg, var(--gold-light), var(--gold) 50%, var(--gold-dark)); display: flex; align-items: center; justify-content: center; color: var(--white); font-size: 36px; letter-spacing: .01em; }
  .label-white .claim { position: absolute; top: 16px; left: 0; right: 0; font-size: 17px; }
  .label-white .dose-pill { position: absolute; top: 74px; left: 50%; transform: translateX(-50%); width: 178px; height: 76px; }
  .label-white .dose-pill .mg { font-size: 28px; }
  .label-white .dose-pill .thc { font-size: 23px; margin-top: 2px; }
  .label-white .flavour { position: absolute; top: 168px; left: 0; right: 0; font-size: 19px; color: var(--ink); }
  .label-white .supplement { bottom: 0; width: 290px; height: 46px; font-size: 17px; }
</style>
</head>
<body>
<main class="canvas">

  <section class="box" aria-label="Carton layout">
    <div class="panel panel--side">
      <div class="zone-green">
        <div class="brand-seal side-seal"><span class="brand-name">LumiVelle</span></div>
        <p class="warning condensed">Do not exceed suggested use. Pregnant or nursing women should consult a physician before using this product. Individuals who have a health condition or are taking medication(s) should check with their physician before use. Immediately discontinue use and consult your physician if any adverse reactions seem to occur. Always check with a physician before starting any dietary supplement regimen.</p>
      </div>
      <div class="zone-gold side-gold">
        <span class="badge" role="img" aria-label="Certification badge"></span>
        <span class="badge" role="img" aria-label="Certification badge"></span>
      </div>
      <div class="zone-white side-white">
        <p class="side-copy side-copy--store condensed">STORE IN A COOL, DARK PLACE. KEEP BOTTLE TIGHTLY CLOSED. KEEP OUT OF THE REACH OF CHILDREN.</p>
        <p class="side-copy side-copy--use condensed">SUGGESTED USE: One serving (2 softgels) per day. See BrightDropRx.com for more suggestions.</p>
        <p class="fda-box condensed">These statements have not been evaluated by the US Food and Drug Administration. This product is not intended to diagnose, treat, cure or prevent any disease.</p>
        <div class="supplement">DIETARY SUPPLEMENT</div>
      </div>
    </div>

    <div class="panel panel--front">
      <div class="zone-green">
        <div class="leaf-mark" role="img" aria-label="Faint hemp leaf decoration"></div>
        <div class="brand-seal front-seal"><span class="brand-name">LumiVelle</span></div>
      </div>
      <div class="zone-gold front-gold serif">
        <span class="kicker">FULL SPECTRUM</span>
        <span class="title">CBD</span>
      </div>
      <div class="zone-white front-white">
        <p class="claim">10X Greater Absorption<br>THAN CBD OILS</p>
        <div class="dose-pill"><span class="mg">500MG</span><span class="thc">THC FREE</span></div>
        <p class="flavour">MINT FLAVOUR</p>
        <div class="supplement">DIETARY SUPPLEMENT</div>
      </div>
    </div>
  </section>

  <section class="label" aria-label="Bottle label">
    <div class="zone-green">
      <div class="brand-seal label-seal"><span class="brand-name">LumiVelle</span></div>
    </div>
    <div class="label-band serif">FULL SPECTRUM CBD</div>
    <div class="zone-white label-white">
      <p class="claim">10X Greater Absorption<br>THAN CBD OILS</p>
      <div class="dose-pill"><span class="mg">500MG</span><span class="thc">THC FREE</span></div>
      <p class="flavour">MINT FLAVOUR</p>
      <div class="supplement">DIETARY SUPPLEMENT</div>
    </div>
  </section>

</main>
</body>
</html>
```